High Quality Business card for Property Management Agency - Super Classy and professional design

High Quality Business card design.

We need a business card designed for our Property Management Agency.
We are located on Sydney's Northern Beaches and manage beautiful properties along the beach and harbor.
We need a design that oozes modern, classy and professional.
I would like it to be double sided with contact details and logo on the front and just the logo on the back.

I need a print ready PDF version of the file as well as an editable photoshop (PSD) version of the file.

Logo and information details attached.

Target Market(s)

Property owners/investors, Male and Female Aged 28-65

Industry/Entity Type

Real Estate

Contact Information for Business Card

Tom Harlow
Tel: 0437 216 590
Email: tom@harlowestates.com.au
Website: www.harlowestates.com.au
Address: Level 2, 17 Kestrel Rd, Wendale NSW 2081

Font styles to use
Sans Serif

Requirements
Must have
• - Logo front and back
• - Business card details listed above and attached
• - Colour
Nice to have
• Sleek and professional

```html
<!DOCTYPE html>
<html lang="en">
<head>
<meta charset="utf-8">
<title>Harlow Estates – Business Card</title>
<link href="https://fonts.googleapis.com/css2?family=Open+Sans:wght@400;600;700&display=swap" rel="stylesheet">
<style>
  :root {
    --backdrop: #2e2825;
    --card-white: #fbfbfa;
    --card-black: #161616;
    --ink: #1c1c1c;
    --ink-soft: #2a2a2a;
    --teal: #1e8f9a;
    --white: #ffffff;
  }
  * { margin: 0; padding: 0; box-sizing: border-box; }
  html, body {
    width: 1200px;
    height: 844px;
    overflow: hidden;
    background: var(--backdrop);
    font-family: "Open Sans", Arial, sans-serif;
  }
  .stage {
    position: relative;
    width: 1200px;
    height: 844px;
  }
  .card {
    position: absolute;
    top: 272px;
    width: 520px;
    height: 300px;
    border-radius: 3px;
    box-shadow: 0 10px 28px rgba(0,0,0,0.45);
    overflow: hidden;
  }
  .card--front {
    left: 60px;
    background: var(--card-white);
  }
  .card--back {
    left: 620px;
    background: var(--card-black);
    display: flex;
    align-items: center;
    justify-content: center;
  }
  .brand {
    display: flex;
    align-items: center;
    gap: 12px;
    font-weight: 700;
    letter-spacing: 0.5px;
    text-transform: uppercase;
    white-space: nowrap;
  }
  .brand__mark {
    width: 14px;
    height: 14px;
    background: var(--teal);
    flex: none;
  }
  .card--front .brand {
    position: absolute;
    left: 34px;
    top: 118px;
    font-size: 32px;
    color: var(--ink);
  }
  .card--back .brand {
    font-size: 34px;
    color: var(--white);
  }
  .card__name {
    position: absolute;
    right: 30px;
    top: 136px;
    font-size: 17px;
    font-weight: 600;
    color: var(--teal);
  }
  .card__rule {
    position: absolute;
    left: 0;
    right: 0;
    top: 166px;
    height: 1.5px;
    background: var(--teal);
  }
  .card__details {
    position: absolute;
    left: 34px;
    top: 184px;
    font-size: 14px;
    line-height: 25px;
    color: var(--ink-soft);
    list-style: none;
  }
  .card__details .sep { margin: 0 6px; }
  .card__details .web { color: var(--teal); }
</style>
</head>
<body>
<main class="stage">
  <section class="card card--front" aria-label="Business card front">
    <div class="brand"><span class="brand__mark"></span>Harlow Estates</div>
    <p class="card__name">Tom Harlow</p>
    <div class="card__rule"></div>
    <ul class="card__details">
      <li>Level 2, 17 Kestrel Rd, Wendale NSW 2081</li>
      <li>0437 216 590<span class="sep">|</span>tom@harlowestates.com.au</li>
      <li class="web">www.harlowestates.com.au</li>
    </ul>
  </section>

  <section class="card card--back" aria-label="Business card back">
    <div class="brand"><span class="brand__mark"></span>Harlow Estates</div>
  </section>
</main>
</body>
</html>
```